Fundraising Study Day East of England. Lift the January blues!

A flyer to advertise a fundraising event of lectures for dental hygienists and therapists in support of the exemption campaign. Currently dental hygienists and therapists require a prescription to deliver certain treatment or recommend certain toothpastes. If we are successful in the campaign we will be able to treat patients without these restrictions.

Industry/Entity Type

Dental

```html
<!DOCTYPE html>
<html lang="en">
<head>
<meta charset="utf-8">
<title>Fundraising Study Day – East of England</title>
<link href="https://fonts.googleapis.com/css2?family=Tinos:wght@400;700&family=Oswald:wght@400;500&display=swap" rel="stylesheet">
<style>
  :root {
    --page-bg: #e9e7e3;
    --paper: #f4f4f5;
    --ink: #2a2a2a;
    --blue: #1d72b8;
    --blue-light: #49a7d9;
    --blue-mid: #2f8cc9;
    --blue-dark: #1b65a8;
    --rule: #3a3a3a;
    --band: #5d5d5f;
    --band-light: #d9d9db;
    --row-text: #2b2b2b;
    --illustration: #c9c3e6;
  }
  * { margin: 0; padding: 0; box-sizing: border-box; }
  html, body { width: 1200px; height: 1000px; overflow: hidden; background: var(--page-bg); }
  .flyer {
    position: absolute; left: 253px; top: 10px; width: 693px; height: 980px;
    background: var(--paper); color: var(--ink);
    font-family: "Tinos", "Times New Roman", serif;
    box-shadow: 0 2px 10px rgba(0,0,0,.15); overflow: hidden;
  }
  .title-bars { position: absolute; left: 0; top: 50px; width: 44px; }
  .title-bars span { display: block; height: 52px; }
  .title-bars .bar-1 { background: var(--blue-light); border-top-right-radius: 22px; }
  .title-bars .bar-2 { background: var(--blue-mid); }
  .title-bars .bar-3 { background: var(--blue-dark); border-bottom-right-radius: 10px; }
  .acrostic { position: absolute; left: 62px; top: 42px; width: 300px; }
  .acrostic-line {
    font-size: 25px; line-height: 1; padding: 8px 0 6px;
    border-bottom: 2px solid var(--blue); margin-bottom: 8px;
  }
  .acrostic-line .initial { color: var(--blue); font-size: 38px; }
  .cartoon {
    position: absolute; left: 370px; top: 40px; width: 230px; height: 115px;
    background: linear-gradient(180deg, #eeedf7, var(--illustration));
    border-radius: 6px;
  }
  .section-title {
    position: absolute; left: 0; width: 100%; text-align: center;
    font-size: 31px; letter-spacing: .5px;
  }
  .section-title.main { top: 228px; left: 70px; }
  .section-title.main::after {
    content: ""; display: block; margin: 4px auto 0; width: 250px; height: 3px;
    background: linear-gradient(90deg, transparent, var(--rule) 25%, var(--rule) 75%, transparent);
  }
  .intro { position: absolute; left: 62px; top: 290px; width: 440px; font-size: 19px; line-height: 1.23; }
  .intro .drop { color: var(--blue); font-size: 30px; font-weight: 700; }
  .intro strong { color: var(--blue); }
  .info-box { position: absolute; border: 1.5px solid #555; background: var(--paper); text-align: center; }
  .info-box h3 { font-size: 15px; font-weight: 700; letter-spacing: .5px; }
  .info-box p { font-size: 17px; line-height: 1.2; }
  .info-box .accent { color: var(--blue); }
  .box-location { left: 150px; top: 500px; width: 130px; padding: 6px 4px; text-align: left; }
  .box-location h3 { text-align: center; }
  .box-cost { left: 303px; top: 485px; width: 95px; padding: 4px; }
  .box-cost h3 { color: var(--blue); font-size: 22px; }
  .box-date { left: 406px; top: 472px; width: 178px; padding: 5px 8px; text-align: left; }
  .box-date h3 { text-align: center; border-bottom: 1.5px solid #555; padding-bottom: 3px; margin-bottom: 3px; }
  .agenda-area {
    position: absolute; left: 0; top: 600px; width: 100%; height: 380px;
    background: linear-gradient(180deg, var(--paper) 0%, #dcdcdf 45%, #c9c9cd 100%);
  }
  .agenda-head { position: absolute; left: 90px; top: 606px; width: 560px; text-align: center; font-size: 20px; letter-spacing: .5px; }
  .agenda-head .sub { display: block; border-top: 1.5px solid var(--rule); margin-top: 2px; padding-top: 3px; }
  .agenda {
    position: absolute; left: 50px; top: 668px; width: 600px; border-collapse: collapse;
    font-family: "Oswald", "Arial Narrow", sans-serif; font-size: 11.5px;
    text-transform: uppercase; color: var(--row-text); line-height: 1.35;
  }
  .agenda td { padding: 3px 8px; vertical-align: middle; border-bottom: 1px solid #9a9a9c; }
  .agenda .time { width: 80px; white-space: nowrap; background: rgba(255,255,255,.45); }
  .agenda .break td { background: var(--band); color: #f1f1f1; text-align: center; font-weight: 500; padding: 4px; }
  .agenda .break .time { text-align: left; }
</style>
</head>
<body>
<main class="flyer">
  <div class="title-bars"><span class="bar-1"></span><span class="bar-2"></span><span class="bar-3"></span></div>
  <div class="acrostic">
    <p class="acrostic-line"><span class="initial">F</span>undraising Study Day</p>
    <p class="acrostic-line"><span class="initial">E</span>ast of England.</p>
    <p class="acrostic-line"><span class="initial">L</span>ift the January blues!</p>
  </div>
  <div class="cartoon" role="img" aria-label="Cartoon of crowded teeth squabbling for space, titled Dental crowding"></div>

  <h2 class="section-title main">DESCRIPTION</h2>
  <p class="intro"><span class="drop">A</span> fundraising event to support our exemptions project. The day will consist of a series of presentations ranging from the new <strong>ECPD</strong> to new technologies. The aim, being to enhance our learning and raise funds to support the exemptions campaign. The speaker line includes some of the <strong>UK</strong> and <strong>Irelands</strong> most respected dental professionals in our field.</p>

  <div class="agenda-area" role="img" aria-label="Faded photo of a dental treatment behind the agenda"></div>

  <div class="info-box box-location">
    <h3>LOCATION</h3>
    <p><span class="accent">L</span>arkfield <span class="accent">H</span>otel<br><span class="accent">O</span>rchard <span class="accent">W</span>ay Hatfield<br><strong class="accent">AL10 4QX</strong></p>
  </div>
  <div class="info-box box-cost">
    <h3>Cost</h3>
    <p>£101.48</p>
  </div>
  <div class="info-box box-date">
    <h3>DATE AND TIME</h3>
    <p><span class="accent">Fri</span> 19 <span class="accent">J</span>anuary 2018<br>09:00 – 16:30 <span class="accent">GMT</span></p>
  </div>

  <div class="agenda-head">DESCRIPTION<span class="sub">AGENDA</span></div>
  <table class="agenda">
    <tr><td class="time">9.30 - 10.15</td><td>Helen Marsh: immediate past president of the BSDP will be updating us on all things ECPD</td></tr>
    <tr><td class="time">10.15 - 11.00</td><td>Rosa Lindqvist: will provide an update on teeth whitening and explain how social media has impacted her business. Clara Whitby: our internationally acclaimed speaker will update our knowledge of periodontal disease and nutrition and new technologies.</td></tr>
    <tr class="break"><td class="time">11.00 - 11.30</td><td>Break</td></tr>
    <tr><td class="time">11.30 - 13.00</td><td>Nora Ashdown &amp; Tessa Hollins: will be providing a combined presentation on 'scaling your business' and start to finish SonicPro techniques. The aim being to build our business with effective communications, systems and protocols. This sessions promises audience participation!</td></tr>
    <tr class="break"><td class="time">12.00 - 14.00</td><td>Lunch</td></tr>
    <tr><td class="time">14.00 - 15.00</td><td>Sam Okafor: save your back. All things posture.</td></tr>
    <tr class="break"><td class="time">15.00 - 15.30</td><td>Break</td></tr>
    <tr><td class="time">15.30 - 16.30</td><td>Clara Whitby: our internationally acclaimed speaker will update our knowledge of periodontal disease and nutrition and new technologies.</td></tr>
  </table>
</main>
</body>
</html>
```